Kestrel Path Business card

We are a company that owns 2 compliance software programs for TV, Radio and Cable industries as well as an online job board. We need a professional business card that incorproates all three logos.

```html
<!DOCTYPE html>
<html lang="en">
<head>
<meta charset="utf-8">
<title>Kestrel Path Business Card</title>
<link href="https://fonts.googleapis.com/css2?family=Montserrat:wght@600;700&family=Open+Sans:wght@400;600&display=swap" rel="stylesheet">
<style>
  :root {
    --navy: #1f1f6b;
    --orange: #e8542a;
    --sky: #2f86d1;
    --ink: #1c1c22;
    --rule: #b9b9c0;
    --paper: #ffffff;
    --backdrop: #e4e5ea;
  }
  * { box-sizing: border-box; margin: 0; padding: 0; }
  html, body { width: 1200px; height: 896px; overflow: hidden; }
  body {
    background: var(--backdrop);
    font-family: "Open Sans", Arial, sans-serif;
    color: var(--ink);
    display: flex;
    flex-direction: column;
    align-items: center;
    justify-content: center;
    gap: 44px;
  }
  .card {
    position: relative;
    width: 660px;
    height: 377px;
    background: var(--paper);
    border-bottom: 16px solid var(--navy);
    box-shadow: 0 6px 18px rgba(0,0,0,.12);
    overflow: hidden;
  }
  .brand-row {
    position: absolute;
    display: flex;
    align-items: center;
  }
  .card-front .brand-row { top: 46px; right: 34px; }
  .card-back .brand-row { top: 120px; left: 50%; transform: translateX(-50%); }
  .brand {
    display: flex;
    align-items: center;
    gap: 8px;
    font-family: "Montserrat", Arial, sans-serif;
    font-weight: 700;
    font-size: 19px;
    color: var(--navy);
    white-space: nowrap;
    padding: 0 16px;
  }
  .brand-dot { width: 12px; height: 12px; border-radius: 50%; }
  .brand-dot.orange { background: var(--orange); }
  .brand-dot.sky { background: var(--sky); }
  .brand-divider { width: 2px; height: 56px; background: var(--navy); }
  .holder {
    position: absolute;
    top: 128px;
    left: 50px;
  }
  .holder-name {
    font-family: "Montserrat", Arial, sans-serif;
    font-weight: 700;
    font-size: 24px;
    letter-spacing: .5px;
    color: var(--navy);
  }
  .holder-role { font-size: 15px; margin-top: 2px; }
  .contact-list { list-style: none; margin-top: 14px; font-size: 15px; }
  .contact-list li { display: flex; align-items: center; gap: 8px; line-height: 24px; }
  .contact-list svg { width: 13px; height: 13px; fill: var(--navy); }
  .card-rule {
    position: absolute;
    left: 50px; right: 40px; top: 284px;
    height: 1px; background: var(--rule);
  }
  .address {
    position: absolute;
    right: 40px; top: 298px;
    text-align: right;
    font-size: 16px;
    line-height: 24px;
  }
  .web {
    position: absolute;
    top: 236px; left: 0; right: 0;
    text-align: center;
    font-size: 18px;
    color: var(--navy);
    letter-spacing: .5px;
  }
</style>
</head>
<body>
  <section class="card card-front" aria-label="Card front">
    <div class="brand-row">
      <div class="brand"><span class="brand-dot orange"></span>Kestrel Path</div>
      <span class="brand-divider"></span>
      <div class="brand"><span class="brand-dot orange"></span>Harrowline</div>
      <span class="brand-divider"></span>
      <div class="brand"><span class="brand-dot sky"></span>Crewline Jobs</div>
    </div>
    <div class="holder">
      <h1 class="holder-name">DARA WHITLOW</h1>
      <p class="holder-role">Managing Director</p>
      <ul class="contact-list">
        <li><svg viewBox="0 0 16 16"><path d="M3 1h3l1 4-2 1a9 9 0 0 0 5 5l1-2 4 1v3c0 1-1 2-2 2A13 13 0 0 1 1 3c0-1 1-2 2-2z"/></svg>044-555 010 222</li>
        <li><svg viewBox="0 0 16 16"><path d="M4 0h8a1 1 0 0 1 1 1v14a1 1 0 0 1-1 1H4a1 1 0 0 1-1-1V1a1 1 0 0 1 1-1zm1 2v10h6V2zm3 11a1 1 0 1 0 0 2 1 1 0 0 0 0-2z"/></svg>044-555 010 223</li>
        <li><svg viewBox="0 0 16 16"><path d="M0 3h16v10H0zm1 1v1l7 4 7-4V4zm0 2.3V12h14V6.3L8 10.3z"/></svg>info@kestrelpath.com</li>
      </ul>
    </div>
    <div class="card-rule"></div>
    <p class="address">48 Harbor Lane<br>Ashford, 20418</p>
  </section>

  <section class="card card-back" aria-label="Card back">
    <div class="brand-row">
      <div class="brand"><span class="brand-dot orange"></span>Kestrel Path</div>
      <span class="brand-divider"></span>
      <div class="brand"><span class="brand-dot orange"></span>Harrowline</div>
      <span class="brand-divider"></span>
      <div class="brand"><span class="brand-dot sky"></span>Crewline Jobs</div>
    </div>
    <p class="web">www.kestrelpath.com</p>
  </section>
</body>
</html>
```